Skincare Clinic specializing in treating difficult skin conditions needs a web design

We want to restructure and rehash our current webdesigns. The current ones are dated and look very old fashioned also, they are not structured well.

The current websites need to get an uplift in look and become more classy and modern with navigation ease by structuring the information into ease of access

The current web address is
www.brightlumera.com.au and
www.velorandum.com.au

We also have international Partner website which is good and we need to better than them. So this website will act as a guide to better the new site
www.tenvora-drholbrook.com

But the new site should be more inclined towards a Blue colour or Aqua marine blue orientation and it needs to be Scientific giving authenticity to the medical industry we operate in.

Attached is a webdesign framework and architecture we would want to adopt. It is a schematic diagram and you can creatively adopt based on what you want to propose.

The website needs to be coded and Should be coded in WordPress such that it helps with SEO activity and google adwords pickup.

We will need the necessary pictures and we could provide them or agree to by them from the designers source.

Target Market(s)

Patients with Skin Disease and people interested to book consultation or buy products for their Skin condition

Industry/Entity Type

Clinic

Coding

Coded - Design and coding required

Number of Pages Required

5+ page

Font styles to use
Other font styles liked:
• Use a light font denoting class.

Requirements
Must have
• Should be modern, Easy to navigate, mobile friendly and coded in wordpress
• Blue colour and should look scientific and medicinal
Nice to have
• Classy and creative
Should not have
• No Green colour or herbal look

```html
<!DOCTYPE html>
<html lang="en">
<head>
<meta charset="utf-8">
<title>brightlumera — Velorandum Skin Clinic</title>
<link href="https://fonts.googleapis.com/css2?family=Open+Sans:wght@300;400;600;700;800&display=swap" rel="stylesheet">
<style>
:root{
  --aqua:#33bfdc;
  --aqua-deep:#06a9e6;
  --aqua-pale:#bfe9f6;
  --aqua-soft:#b9e3ec;
  --panel:#e1ebef;
  --ink:#1b1b1b;
  --text:#333;
  --footer:#3190b8;
  --footer-bar:#27769a;
  --footer-text:#cfe6f1;
  --grey-icon:#9ea4a7;
  --link:#2aaed3;
}
*{box-sizing:border-box;margin:0;padding:0}
html,body{width:1097px;height:1200px;overflow:hidden;background:#fff;font-family:"Open Sans",sans-serif;color:var(--text)}
.page{position:relative;width:1097px;height:1200px}
.abs{position:absolute}

.brand{left:100px;top:28px;display:flex;align-items:center;gap:12px}
.brand-name{font-size:32px;font-weight:700;color:var(--aqua);line-height:1}
.brand-sub{font-size:15px;font-weight:600;color:#555;margin-top:4px;letter-spacing:-.2px}
.brand-mark{width:40px;height:40px;border-radius:50%;background:var(--aqua-deep)}

.motto{left:466px;top:13px;width:530px;height:84px;background:linear-gradient(90deg,#38bff0 0%,#4cc4ef 55%,#8fd5ef 80%,#5cc6ee 100%);padding:14px 0 0 46px;color:#fff}
.motto .q{position:absolute;left:24px;top:2px;font-size:26px;font-weight:800;font-style:italic}
.motto p{font-size:14.5px;font-weight:700;line-height:17px}
.motto strong{display:block;font-size:26px;font-weight:800;color:#fff;line-height:28px}
.motto strong span{color:#0d5a8c}

.nav{left:97px;top:99px;width:899px;height:44px;border:3px solid #9ee0f0;background:var(--aqua);display:flex;align-items:center;justify-content:space-around;padding:0 40px}
.nav a{color:#fff;text-decoration:none;font-size:14.5px;padding:5px 19px}
.nav a.active{background:var(--aqua-soft);color:#1d4a55}

.hero{left:97px;top:147px;width:899px;height:231px;border:3px solid #a3e1f1;background:linear-gradient(90deg,#e2d8cd 0%,#e7e2dc 55%,#d6c8bc 100%)}
.hero-photo{position:absolute;right:50px;top:0;width:320px;height:225px;background:radial-gradient(ellipse at 55% 45%,#c79a7c 0%,#b7876a 40%,rgba(215,200,188,0) 72%)}
.hero-copy{position:absolute;left:23px;top:99px;color:var(--ink)}
.hero-copy p{font-size:21px;font-weight:300;line-height:26px}
.hero-copy strong{display:block;font-size:21px;font-weight:800;margin-top:2px}
.dots{position:absolute;right:7px;top:148px;display:flex;flex-direction:column;gap:6px}
.dots i{width:10px;height:10px;border-radius:50%;border:1px solid var(--aqua);background:#fff;display:block}
.dots i.on{background:var(--aqua)}

.actions{left:97px;top:395px;width:899px;height:156px;background:var(--aqua-pale)}
.action{position:absolute;top:14px;width:228px;height:126px;background:#fff;text-align:center;padding-top:12px}
.action.book{background:var(--aqua)}
.action .ic{width:48px;height:48px;border-radius:50%;background:var(--grey-icon);margin:0 auto;display:flex;align-items:center;justify-content:center}
.action.book .ic{background:#fff}
.action small{display:block;font-size:12px;font-weight:600;color:var(--ink);margin-top:11px}
.action b{display:block;font-size:21px;font-weight:400;color:var(--ink);margin-top:1px}

.doctor{left:97px;top:574px;width:433px;height:187px;background:var(--panel)}
.doctor-head{position:absolute;left:0;top:0;width:433px;height:46px;background:var(--aqua-deep);padding:15px 0 0 33px;font-size:13px;font-weight:700;color:var(--ink)}
.doctor-photo{position:absolute;left:18px;top:54px;width:130px;height:129px;background:linear-gradient(180deg,#ddd 0%,#a59a92 45%,#4a4c50 100%)}
.doctor-text{position:absolute;left:159px;top:63px;width:265px;font-size:10.5px;line-height:15.5px;color:#222}
.more{display:inline-block;margin-top:9px;color:var(--link);font-size:12px}

.cases{left:548px;top:574px;width:448px;height:187px;background:var(--panel)}
.cases-head{position:absolute;left:0;top:0;width:448px;height:46px;background:var(--aqua);color:#fff;font-size:15px;font-weight:800;padding-top:14px;padding-left:148px;display:flex;gap:8px}
.cases-text{position:absolute;left:23px;top:71px;width:200px;font-size:10.5px;line-height:15.5px;color:#222}
.btn{position:absolute;left:23px;top:157px;background:var(--aqua-deep);color:#fff;font-size:11.5px;padding:3px 8px;border-radius:2px}
.label{position:absolute;top:51px;font-size:16px;color:var(--ink)}
.shot{position:absolute;top:75px;width:101px;height:93px}

.quote{left:180px;top:816px;width:737px;height:101px;background:var(--panel);text-align:center}
.bump{left:477px;top:787px;width:118px;height:60px;border-radius:59px 59px 0 0;background:#c8d1d5;display:flex;justify-content:center;padding-top:17px}
.arrows{position:absolute;left:12px;top:7px;display:flex;gap:4px}
.quote h4{position:absolute;top:47px;width:100%;color:#1b8eb8;font-size:12.5px;font-weight:600}
.quote p{position:absolute;top:68px;left:40px;width:657px;font-size:10.5px;line-height:15.5px;color:#333}

.footer{left:0;top:936px;width:1097px;height:217px;background:var(--footer)}
.col{position:absolute;top:20px;padding-right:20px;height:180px;border-right:1px solid #4aa1c6}
.col h5{font-size:12.5px;font-weight:400;color:#e7f3f8;margin-bottom:17px}
.col li{list-style:none;font-size:10.5px;line-height:20.6px;color:var(--footer-text)}
.col li::before{content:"›";font-weight:800;margin-right:6px}
.col li.hi{color:#fff}
.col li.cont::before{content:"";margin-right:14px}
.col.last{border-right:none}
.bar{left:0;top:1153px;width:1097px;height:47px;background:var(--footer-bar);color:#173f55;font-size:10.5px}
.bar .l{position:absolute;left:97px;top:17px}
.bar .r{position:absolute;right:97px;top:17px}
.social{position:absolute;top:13px;display:flex;gap:5px}
.social i{width:20px;height:20px;background:#e8eef1;border:1px solid #1e5f7c;display:block}
</style>
</head>
<body>
<div class="page">

  <div class="abs brand">
    <div>
      <div class="brand-name">brightlumera</div>
      <div class="brand-sub">by Velorandum Skin Clinic</div>
    </div>
    <span class="brand-mark"></span>
  </div>

  <div class="abs motto">
    <span class="q">“</span>
    <p>BE EVERYWHERE,<br>DOEVERYTHING,AND NEVER FAIL TO</p>
    <strong>THE <span>CUSTOMER</span></strong>
  </div>

  <nav class="abs nav">
    <a href="#">About Us</a><a href="#" class="active">Treatments</a><a href="#">Products</a><a href="#">Results</a><a href="#">Media Skin</a><a href="#">Conditions</a>
  </nav>

  <section class="abs hero">
    <div class="hero-photo" role="img" aria-label="Photo of a young woman covering her mouth with her hands"></div>
    <div class="hero-copy">
      <p>EMBARASSED<br>YOUR SKIN CONDITION?</p>
      <strong>YOUR FATURE IS CLEAR WITH US,NATURALLY</strong>
    </div>
    <div class="dots"><i></i><i></i><i class="on"></i><i></i><i></i></div>
  </section>

  <section class="abs actions">
    <div class="action book" style="left:49px">
      <div class="ic"><svg width="24" height="24" viewBox="0 0 24 24" fill="none" stroke="#333" stroke-width="2"><path d="M5 3v6a4 4 0 008 0V3M9 13v3a4 4 0 008 0v-3"/><circle cx="17" cy="10" r="2.5"/></svg></div>
      <small>CONSULTATION</small><b>BOOK ONLINE</b>
    </div>
    <div class="action" style="left:331px">
      <div class="ic"><svg width="22" height="20" viewBox="0 0 22 20"><rect x="1" y="5" width="20" height="14" rx="1" fill="#222"/><rect x="7" y="1" width="8" height="5" fill="none" stroke="#222" stroke-width="2"/><path d="M11 16l-4-4a2 2 0 013-3l1 1 1-1a2 2 0 013 3z" fill="#fff"/></svg></div>
      <small>PURCHASE</small><b>PRODUCTS ONLINE</b>
    </div>
    <div class="action" style="left:613px">
      <div class="ic"><svg width="24" height="18" viewBox="0 0 24 18" stroke="#222" stroke-width="1.6"><path d="M2 9h2M6 6v6M9 3v12M12 1v16M15 4v10M18 6v6M21 9h2"/></svg></div>
      <small>PRACTITIONERS</small><b>INTRANET ACCESS</b>
    </div>
  </section>

  <section class="abs doctor">
    <div class="doctor-head">Dr Martin Holbrook</div>
    <div class="doctor-photo" role="img" aria-label="Portrait photo of the clinic founder in a suit"></div>
    <div class="doctor-text">
      Medical Research Scientist and Founder of Velorandum Skin Clinic, with clinics located throughout Australia and New Zealand.Medical Research Scientist and Founder of Velorandum Skin Clinic, with clinics located throughout Australia and New Zealand.
      <br><a class="more">READ MORE</a>
    </div>
  </section>

  <section class="abs cases">
    <div class="cases-head">
      <svg width="22" height="22" viewBox="0 0 22 22"><path d="M3 19l1-5L15 3l4 4L8 18z" fill="#111"/></svg>
      CASE STUDIES
    </div>
    <p class="cases-text">These before and after photographs have been taken at the time of patient consultations and record the progress of the patient's response to the treatment protocols.</p>
    <span class="btn">MORE GALLERY</span>
    <span class="label" style="left:248px">Before</span>
    <span class="label" style="left:366px">After</span>
    <div class="shot" role="img" aria-label="Before photo of a patient's cheek with acne" style="left:227px;background:linear-gradient(135deg,#c98d78,#b06a58 60%,#7a4a40)"></div>
    <div class="shot" role="img" aria-label="After photo of the same patient with clear skin" style="left:336px;background:linear-gradient(135deg,#c9b4aa,#e6cfc4 55%,#b79684)"></div>
  </section>

  <div class="abs bump"><svg width="32" height="20" viewBox="0 0 32 20" fill="#111"><circle cx="9" cy="6" r="4"/><circle cx="23" cy="6" r="4"/><circle cx="16" cy="5" r="4.5"/><path d="M1 19c0-6 4-8 8-8s8 2 8 8zM15 19c0-6 4-8 8-8s8 2 8 8z"/><path d="M7 19c0-7 4-9 9-9s9 2 9 9z"/></svg></div>
  <section class="abs quote">
    <div class="arrows">
      <svg width="20" height="16" viewBox="0 0 20 16" fill="#2ab6d8"><path d="M0 5h10V0l10 8-10 8v-5H0z"/></svg>
      <svg width="20" height="16" viewBox="0 0 20 16" fill="#2ab6d8"><path d="M20 5H10V0L0 8l10 8v-5h10z"/></svg>
    </div>
    <h4>P.O, Victoria, Australia</h4>
    <p>"I've had psoriasis for over 25 years and used all the recommended forms of treatment. After using Dr. Holbrook's within three weeks I was well on my way to being psoriasis free."</p>
  </section>

  <footer class="abs footer">
    <div class="col" style="left:99px;width:165px"><h5>About Us</h5><ul>
      <li>Introduction</li><li>History</li><li>Our Founder</li><li>Our Treatment Protocol</li><li>Our Logo</li><li>International Partnership</li><li>Contact Details</li></ul></div>
    <div class="col" style="left:290px;width:177px"><h5>Treatment Protocol</h5><ul>
      <li>What do we specialise on</li><li>Consultations</li><li>5 Unique steps involved</li><li class="hi">Book an appointment</li><li>Clinic Location</li><li>Practitioners and associates</li><li>Cost of Consultation</li></ul></div>
    <div class="col" style="left:494px;width:180px"><h5>Products</h5><ul>
      <li>Introduction</li><li>Safety profile and test</li><li>Orals</li><li>Topicals</li><li>Others</li><li>Distributors</li><li>Distribution opportunities</li></ul></div>
    <div class="col" style="left:698px;width:157px"><h5>Results</h5><ul>
      <li>Clinical Trails</li><li>Case Studies</li><li>Before and After Photos</li><li>Patient Testimonials</li><li>Media exposure</li></ul></div>
    <div class="col last" style="left:870px;width:140px"><h5>Skin Conditions</h5><ul>
      <li>Psoriasis</li><li>Eczema</li><li>Rosacea</li><li>Other Common</li><li class="cont">Skin conditions</li></ul></div>
  </footer>

  <div class="abs bar">
    <span class="l">Disclaimer | Privacy</span>
    <div class="social" style="left:387px"><i></i><i></i><i></i></div>
    <div class="social" style="left:500px"><i></i><i></i><i></i></div>
    <span class="r">Copyright Pracitioner Login | Webmail</span>
  </div>

</div>
</body>
</html>
```